Zielgruppe
Wir sind eine Unternehmsberatung für ambulante Pflegedienste. Es wird ein Flyer und eine Anzeige in gleichem Design benötigt
Aufgabenstellung
Vorderseite
Headline / Titel
KOLUNE – Unternehmensberatung für ambulante Pflegedienste
Sub Headline / Slogan
Wirtschaftlichkeit stärken. Prozesse optimieren. Zukunft sichern.
Kurze Einführung / Elevator Pitch
Sie sind Pflegedienst Inhaber*in oder Führungskraft und stehen täglich vor wirtschaftlichen Herausforderungen?
Unser interdisziplinäres Experten Team von Kolune analysiert Ihre Tourenpläne, Leistungskalkulationen und Kennzahlen – und zeigt, wie Sie Ihre Pflege¬leistungen ökonomisch optimieren und gleichzeitig Ihre Pflegequalität sichern.
Leistungen im Überblick
Unsere Beratungsfelder im Überblick:
• Tourenplananalyse & Routenoptimierung
Wir untersuchen Fahr und Besuchsstrukturen, identifizieren Leerlauf, optimieren Einsatzzeiten und steigern die Effizienz.
• Kosten und Leistungsrechnung
Wir prüfen Ihre Kostenstruktur, Leistungserfassung und Vergütungsmodelle – um optimale Deckungsbeiträge zu erreichen.
• Kennzahlen Monitoring
Von Pflegestunden pro Klient bis Personalkostenquote – wir definieren die relevanten KPIs, vergleichen Soll Ist Werte und entwickeln praxisnahe Maßnahmen.
• Prozess und Organisationsberatung
Wir begleiten Sie bei der Digitalisierung, dem QM System, Personalmanagement und bei strategischen Entscheidungen (z. B. Expansion, Kooperationen).
Warum Kolune?
• Erfahren & praxisnah: Unser Team besteht aus ehemaligen Leitungskräften, Pflegefachkräften und Betriebswirt*innen mit Fokus auf ambulante Pflege.
• 100 % professionell geführt: Wir arbeiten strukturiert, belastbar und transparent – analog zu den hohen Anforderungen in Ihrem Alltag.
• Maßgeschneiderte Lösungen: Keine Standardberatung, sondern passgenau für Ihre Strukturen – sofort umsetzbar.
Jetzt Erstgespräch anfragen – kostenf..

```html
<!DOCTYPE html>
<html lang="de">
<head>
<meta charset="UTF-8">
<title>Kolune – Flyer Vorder- und Rückseite</title>
<link href="https://fonts.googleapis.com/css2?family=Rubik:wght@400;500;600&display=swap" rel="stylesheet">
<style>
:root{
  --navy:#27466b;
  --orange:#ef7622;
  --lavender:#dedaea;
  --red:#d63a55;
  --text:#4d4d4d;
  --bg:#eef0f3;
  --white:#ffffff;
}
*{margin:0;padding:0;box-sizing:border-box}
html,body{width:1001px;height:1200px;overflow:hidden}
body{background:var(--bg);font-family:"Rubik",sans-serif;position:relative}
.page{position:absolute;top:267px;width:470px;height:666px;background:var(--white);box-shadow:0 4px 14px rgba(0,0,0,.18);overflow:hidden}
.front{left:18px}
.back{left:512px}

/* front */
.brand{position:absolute;top:40px;left:0;width:100%;text-align:center;font-size:40px;font-weight:500;color:var(--navy);letter-spacing:2px}
.hero{position:absolute;top:0;left:0}
.headline{position:absolute;top:420px;left:0;width:100%;text-align:center;font-size:26px;line-height:31px;font-weight:600;color:var(--navy)}
.claims{position:absolute;top:508px;left:0;width:100%;height:77px;display:flex}
.claim{display:flex;align-items:center;justify-content:center;text-align:center;font-size:13.5px;line-height:16px;font-weight:500}
.claim-1{width:166px;background:var(--lavender);color:var(--navy)}
.claim-2{width:138px;background:var(--navy);color:var(--white)}
.claim-3{width:166px;background:var(--orange);color:var(--white)}
.url{position:absolute;top:622px;width:100%;text-align:center;font-size:12px;font-weight:500;color:var(--navy)}

/* back */
.pitch{position:absolute;top:0;left:0;width:100%;height:148px;background:var(--navy);color:var(--white);padding:30px 30px 0}
.pitch h2{font-size:14px;font-weight:500;margin-bottom:10px}
.pitch p{font-size:8.6px;line-height:12.5px;margin-bottom:12px}
.section-title{position:absolute;left:30px;font-size:13px;font-weight:500;color:var(--navy)}
.fields{position:absolute;top:195px;left:30px;right:26px}
.field{display:flex;gap:11px;margin-bottom:13px}
.field svg{flex:0 0 28px;margin-top:2px}
.field h3{font-size:10.4px;font-weight:500;color:#333;margin-bottom:2px}
.field p{font-size:8.8px;line-height:12.5px;color:var(--text)}
.reasons{position:absolute;top:480px;left:20px;right:20px;display:flex}
.reason{flex:1;text-align:center;padding:0 6px}
.reason h4{font-size:9.6px;line-height:12px;font-weight:500;color:var(--navy);margin:6px 0 12px}
.reason p{font-size:8px;line-height:11px;color:var(--text)}
.cta{position:absolute;left:0;bottom:0;width:100%;height:52px;background:var(--red);color:var(--white);display:flex;align-items:center;justify-content:space-between;padding:0 30px}
.cta strong{font-size:12px;line-height:16px;font-weight:500}
.cta .contact{font-size:8px;line-height:14px;font-weight:500;width:150px}
</style>
</head>
<body>

<section class="page front">
  <svg class="hero" width="470" height="400" viewBox="0 0 470 400">
    <defs>
      <linearGradient id="heroTone" x1="0" y1="0" x2="1" y2="1">
        <stop offset="0" stop-color="#c9d0d6"/>
        <stop offset=".45" stop-color="#8d9fb2"/>
        <stop offset="1" stop-color="#5d7fa8"/>
      </linearGradient>
    </defs>
    <path role="img" aria-label="Foto: Pflegefachkraft berät ein älteres Paar am Tisch mit einem Tablet" d="M0 87 Q235 165 470 85 L470 353 Q235 425 0 353 Z" fill="url(#heroTone)"/>
    <path d="M0 87 Q235 165 470 85" fill="none" stroke="var(--red)" stroke-width="2"/>
  </svg>
  <div class="brand">KOLUNE</div>
  <h1 class="headline">UNTERNEHMENSBERATUNG FÜR<br>AMBULANTE PFLEGEDIENSTE</h1>
  <div class="claims">
    <div class="claim claim-1">Wirtschaftlichkeit<br>stärken.</div>
    <div class="claim claim-2">Prozesse<br>optimieren.</div>
    <div class="claim claim-3">Zukunft<br>sichern.</div>
  </div>
  <div class="url">www.KOLUNE.de</div>
</section>

<section class="page back">
  <div class="pitch">
    <h2>Kurze Einführung / Elevator Pitch</h2>
    <p>Sie sind Pflegedienst Inhaber*in oder Führungskraft und stehen täglich vor wirtschaftlichen Herausforderungen?</p>
    <p>Unser interdisziplinäres Experten Team von Kolune analysiert Ihre Tourenpläne, Leistungskalkulationen und Kennzahlen – und zeigt, wie Sie Ihre Pflege­leistungen ökonomisch optimieren und gleichzeitig Ihre Pflegequalität sichern.</p>
  </div>

  <h2 class="section-title" style="top:160px">Unsere Beratungsfelder im Überblick:</h2>
  <div class="fields">
    <div class="field">
      <svg width="28" height="28" viewBox="0 0 28 28" fill="none" stroke="var(--orange)" stroke-width="1.3"><rect x="2" y="3" width="24" height="22" rx="2"/><path d="M6 20 Q10 12 14 16 T22 8"/><circle cx="6" cy="20" r="1.6"/><circle cx="22" cy="8" r="1.6"/></svg>
      <div><h3>Tourenplananalyse &amp; Routenoptimierung</h3><p>Wir untersuchen Fahr und Besuchsstrukturen, identifizieren Leerlauf, optimieren Einsatzzeiten und steigern die Effizienz.</p></div>
    </div>
    <div class="field">
      <svg width="28" height="28" viewBox="0 0 28 28" fill="none" stroke="var(--orange)" stroke-width="1.3"><circle cx="8" cy="15" r="5"/><circle cx="17" cy="12" r="5"/><circle cx="22" cy="21" r="3"/><path d="M8 13v4M17 10v4"/></svg>
      <div><h3>Kosten und Leistungsrechnung</h3><p>Wir prüfen Ihre Kostenstruktur, Leistungserfassung und Vergütungsmodelle – um optimale Deckungsbeiträge zu erreichen.</p></div>
    </div>
    <div class="field">
      <svg width="28" height="28" viewBox="0 0 28 28" fill="none" stroke="var(--orange)" stroke-width="1.3"><rect x="2" y="4" width="24" height="16" rx="1.5"/><path d="M14 20v4M9 24h10M6 9h7M6 12h7M6 15h7M17 16v-4M20 16v-6M23 16v-3"/></svg>
      <div><h3>Kennzahlen Monitoring</h3><p>Von Pflegestunden pro Klient bis Personalkostenquote – wir definieren die relevanten KPIs, vergleichen Soll Ist Werte und entwickeln praxisnahe Maßnahmen.</p></div>
    </div>
    <div class="field">
      <svg width="28" height="28" viewBox="0 0 28 28" fill="none" stroke="var(--orange)" stroke-width="1.3"><circle cx="5" cy="6" r="2.5"/><rect x="11" y="3" width="7" height="6" rx="1"/><circle cx="23" cy="6" r="2.5"/><rect x="3" y="15" width="7" height="6" rx="1"/><circle cx="16" cy="18" r="2.5"/><rect x="19" y="15" width="7" height="6" rx="1"/><path d="M7.5 6h3.5M18 6h2.5M14 9v6M10 18h3.5M18.5 18h.5"/></svg>
      <div><h3>Prozess und Organisationsberatung</h3><p>Wir begleiten Sie bei der Digitalisierung, dem QM System, Personalmanagement und bei strategischen Entscheidungen (z.B. Expansion, Kooperationen).</p></div>
    </div>
  </div>

  <h2 class="section-title" style="top:446px">Warum Kolune?</h2>
  <div class="reasons">
    <div class="reason">
      <svg width="18" height="14" viewBox="0 0 18 14"><path d="M2 7l5 5L16 2" fill="none" stroke="var(--navy)" stroke-width="3"/></svg>
      <h4>Erfahren &amp;<br>praxisnah</h4>
      <p>Unser Team besteht aus ehemaligen Leitungskräften, Pflegefachkräften und Betriebswirt*innen mit Fokus auf ambulante Pflege.</p>
    </div>
    <div class="reason">
      <svg width="18" height="14" viewBox="0 0 18 14"><path d="M2 7l5 5L16 2" fill="none" stroke="var(--navy)" stroke-width="3"/></svg>
      <h4>100% professionell<br>geführt</h4>
      <p>Wir arbeiten strukturiert, belastbar und transparent – analog zu den hohen Anforderungen in Ihrem Alltag.</p>
    </div>
    <div class="reason">
      <svg width="18" height="14" viewBox="0 0 18 14"><path d="M2 7l5 5L16 2" fill="none" stroke="var(--navy)" stroke-width="3"/></svg>
      <h4>Maßgeschneiderte<br>Lösungen</h4>
      <p>Keine Standardberatung, sondern passgenau für Ihre Strukturen – sofort umsetzbar.</p>
    </div>
  </div>

  <div class="cta">
    <strong>Jetzt Erstgespräch anfragen<br>kostenfrei &amp; unverbindlich</strong>
    <div class="contact">info@kolune.de &nbsp;I&nbsp; 0381 55820147<br>Lindenweg 12 in 18057 Rostock</div>
  </div>
</section>

</body>
</html>
```